K9R Business Cards

Business Cards

Contact Information for Business Card

Company name, owner name, license #s, phone & email

Requirements
Should not have
• mailing address

```html
<!DOCTYPE html>
<html lang="en">
<head>
<meta charset="utf-8">
<title>K9R Realty Business Card</title>
<link href="https://fonts.googleapis.com/css2?family=Arimo:wght@400;700&display=swap" rel="stylesheet">
<style>
  :root {
    --bg: #c9c9c9;
    --card-white: #ffffff;
    --brand-blue: #1b3c96;
    --deep-blue: #16338a;
    --accent-red: #d8232a;
    --ink: #2a2a2a;
    --rule: #4a62a8;
    --photo-tone: #d9d6d3;
  }
  * { margin: 0; padding: 0; box-sizing: border-box; }
  html, body { width: 1200px; height: 788px; overflow: hidden; }
  body {
    background: var(--bg);
    font-family: "Arimo", Arial, sans-serif;
    position: relative;
  }
  .card {
    position: absolute;
    top: 240px;
    width: 540px;
    height: 309px;
    border-radius: 18px;
    overflow: hidden;
    box-shadow: 0 10px 24px rgba(0,0,0,0.28);
  }
  .card-front { left: 40px; background: var(--card-white); }
  .card-back { left: 620px; }

  .edge-band {
    position: absolute;
    left: 0; bottom: 0;
    width: 100%; height: 9px;
  }

  .brand-name {
    position: absolute;
    left: 30px; top: 58px;
    color: var(--brand-blue);
    font-weight: 700;
    font-size: 38px;
    line-height: 1;
    letter-spacing: 1px;
  }
  .agent-photo {
    position: absolute;
    right: 36px; top: 22px;
    width: 130px; height: 92px;
    border-radius: 10px;
    background: linear-gradient(180deg, var(--photo-tone) 0%, #b9b4b0 60%, #2b2b2e 100%);
  }
  .agent-name {
    position: absolute;
    left: 30px; top: 152px;
    color: var(--brand-blue);
    font-weight: 700;
    font-size: 27px;
    line-height: 1.1;
    letter-spacing: 0.5px;
  }
  .license-list {
    position: absolute;
    right: 36px; top: 148px;
    list-style: none;
    text-align: right;
    font-size: 13px;
    line-height: 1.45;
    color: var(--ink);
  }
  .divider {
    position: absolute;
    left: 30px; right: 24px; top: 192px;
    height: 1px;
    background: var(--rule);
  }
  .contact-list {
    position: absolute;
    left: 30px; top: 206px;
    list-style: none;
  }
  .contact-list li {
    display: flex; align-items: center;
    gap: 8px;
    font-size: 16px;
    line-height: 1.2;
    color: var(--ink);
    margin-bottom: 8px;
  }
  .contact-icon {
    width: 18px; height: 18px;
    border-radius: 50%;
    background: var(--accent-red);
    display: flex; align-items: center; justify-content: center;
    flex: none;
  }
  .email-user { color: var(--accent-red); }

  .back-pattern {
    position: absolute; inset: 0;
    background: linear-gradient(135deg, #5c7fd0 0%, #2446a6 35%, var(--deep-blue) 70%, #1d3b94 100%);
  }
  .back-brand {
    position: absolute;
    right: 40px; bottom: 60px;
    color: var(--card-white);
    font-weight: 700;
    font-size: 20px;
  }
</style>
</head>
<body>
  <section class="card card-front">
    <div class="brand-name">K9R Realty</div>
    <div class="agent-photo" role="img" aria-label="Portrait photo of the agent in a dark suit"></div>
    <h1 class="agent-name">MARK DELANEY</h1>
    <ul class="license-list">
      <li>Lic. # 40718352</li>
      <li>Broker Lic. # 20593146</li>
    </ul>
    <div class="divider"></div>
    <ul class="contact-list">
      <li>
        <span class="contact-icon">
          <svg width="10" height="10" viewBox="0 0 24 24"><path fill="#fff" d="M6.6 10.8a15 15 0 0 0 6.6 6.6l2.2-2.2a1 1 0 0 1 1-.25 11.4 11.4 0 0 0 3.6.6 1 1 0 0 1 1 1V20a1 1 0 0 1-1 1A17 17 0 0 1 3 4a1 1 0 0 1 1-1h3.5a1 1 0 0 1 1 1c0 1.25.2 2.45.6 3.6a1 1 0 0 1-.25 1z"/></svg>
        </span>
        555-014-2870
      </li>
      <li>
        <span class="contact-icon">
          <svg width="10" height="10" viewBox="0 0 24 24"><path fill="#fff" d="M2 5h20v14H2z M2 5l10 8 10-8" stroke="#d8232a" stroke-width="1.5"/></svg>
        </span>
        <span><span class="email-user">Jmarkdelaney</span>@mailbox.com</span>
      </li>
    </ul>
    <svg class="edge-band" viewBox="0 0 540 9" preserveAspectRatio="none">
      <polygon points="0,0 272,0 266,9 0,9" fill="var(--brand-blue)"/>
      <polygon points="272,0 540,0 540,9 266,9" fill="var(--accent-red)"/>
    </svg>
  </section>

  <section class="card card-back">
    <div class="back-pattern" role="img" aria-label="Repeating embossed brand monogram pattern in blue"></div>
    <div class="back-brand">K9R Realty</div>
  </section>
</body>
</html>
```